Willowmere Equine Sanctuary Flyer Urgent

Willowmere Equine Sanctuary

Rescue • Rehabilitation • Sanctuary

Willowmere Equine Sanctuary provides a safe and ethical refuge for horses, ponies and donkeys who have nowhere else to go. Some arrive needing rehabilitation and careful retraining, while others find permanent sanctuary here due to age, injury or behavioural needs.

Our mission is simple: to improve the physical and psychological wellbeing of every animal in our care.

At Willowmere we focus on:
• Rescue and rehabilitation of horses in need
• Lifetime sanctuary for those who cannot be rehomed
• Education and advocacy for responsible horse care
• Equine rehabilitation services to help horses recover and thrive

Sponsor a Horse

One of the most meaningful ways to support our work is by sponsoring one of our residents. Each horse, pony or donkey only has one sponsor!

Your sponsorship helps provide:
• Hay and feed
• Veterinary care
• Hoof trimming and routine health care
• Rugs, shelter and daily care

Many of our horses will live out their lives here, and sponsorship ensures they are safe, well fed and cared for every single day.

Sponsorship starts from $15 - $25 per week / $60 -$100 per month.

How You Can Help

• Sponsor a horse
• Make a donation
• Share our work with others

Your support helps us continue to say yes to horses who need a second chance.

📍 Willowmere Park, Victoria
📧 clara@willowmerepark-example.org

📞 0400 519 627

Font styles to use
Serif
Sans Serif

Colors
F0912C
F2A743
F7CA91
FBE8D2
FDF5EE
EE7325
F08F49
F5BC92
FAE3D3
FDF4ED

Requirements
Should not have
• Photos not provided by Willowmere

```html
<!DOCTYPE html>
<html lang="en">
<head>
<meta charset="utf-8">
<title>Willowmere Equine Sanctuary – Sponsorship Flyer</title>
<link rel="stylesheet" href="https://fonts.googleapis.com/css2?family=Cinzel:wght@400;600;700&family=Crimson+Pro:wght@400;600;700&display=swap">
<style>
  :root {
    --stage: #4a4a4a;
    --paper: #ffffff;
    --orange: #e37c06;
    --orange-light: #f5892f;
    --orange-deep: #c4620a;
    --ink: #1b1b1b;
    --panel: #202020;
    --blue: #1414f0;
    --white: #ffffff;
    --cream: #fde9cf;
    --body: #222222;
  }
  * { box-sizing: border-box; margin: 0; padding: 0; }
  html, body { width: 1200px; height: 1200px; overflow: hidden; background: var(--stage); }
  .flyer {
    position: absolute; left: 228px; top: 74px; width: 744px; height: 1052px;
    background: var(--paper); overflow: hidden;
    font-family: "Crimson Pro", Georgia, serif; color: var(--body);
  }
  .abs { position: absolute; }

  /* Header */
  .header-band { left: 0; top: 0; width: 744px; height: 431px; background: var(--orange); }
  .header-photo {
    left: 576px; top: 0; width: 168px; height: 431px;
    background: linear-gradient(160deg, #9fb3c8 0%, #6b4a3a 35%, #3d2418 70%, #8a7f6a 100%);
  }
  .brand { left: 27px; top: 72px; display: flex; align-items: center; gap: 10px; }
  .brand-name { font-family: "Cinzel", Georgia, serif; font-size: 24px; color: var(--white); font-weight: 400; line-height: 1; }
  .brand-mark { width: 15px; height: 15px; background: var(--white); }
  .title-main { left: 24px; top: 182px; font-family: "Cinzel", Georgia, serif; color: var(--white);
    font-size: 62px; font-weight: 600; line-height: 1; letter-spacing: 1px; }
  .title-sub { left: 25px; top: 302px; font-family: "Cinzel", Georgia, serif; color: var(--white);
    font-size: 33px; font-weight: 400; line-height: 1; letter-spacing: 1px; }
  .tagline { left: 25px; top: 376px; font-family: "Cinzel", Georgia, serif; color: var(--white); font-size: 17px; letter-spacing: .5px; line-height: 22px; }
  .tagline .dot { font-size: 9px; vertical-align: middle; margin: 0 8px; }

  /* Intro */
  .intro {
    left: 27px; top: 452px; width: 372px; padding-left: 16px;
    border-left: 2px solid var(--orange); font-size: 14.3px; line-height: 18px; color: var(--ink);
  }

  /* Sponsor card */
  .sponsor-card { left: 27px; top: 566px; width: 366px; height: 193px; background: var(--panel); }
  .sponsor-photo {
    left: 0; top: 0; width: 224px; height: 193px;
    background: linear-gradient(120deg, #4d5a3a 0%, #8e4a22 40%, #a75a2a 60%, #3a3a2a 100%);
  }
  .sponsor-head { right: 8px; top: 10px; text-align: right; font-family: "Cinzel", Georgia, serif; color: var(--white); font-weight: 400; }
  .sponsor-head .l1 { font-size: 29px; line-height: 30px; }
  .sponsor-head .l2 { font-size: 29px; line-height: 34px; display: flex; align-items: center; justify-content: flex-end; gap: 4px; }
  .sponsor-head .hl { background: var(--orange); font-weight: 600; padding: 0 10px 0 4px; margin-right: -10px; }
  .sponsor-text { left: 225px; top: 90px; width: 136px; color: var(--white); font-size: 11px; line-height: 15px; }

  /* Provides */
  .provides-bar { left: 0; top: 767px; width: 325px; height: 26px; background: var(--blue); color: var(--white);
    font-family: "Cinzel", Georgia, serif; font-size: 15px; font-weight: 400; line-height: 26px; padding-left: 28px; letter-spacing: .3px; }
  .provides-list { left: 27px; top: 802px; width: 380px; display: grid; grid-template-columns: 141px 239px; row-gap: 6px; list-style: none; }
  .provides-list li { display: flex; align-items: center; gap: 8px; color: var(--blue); font-size: 12px; font-weight: 600; height: 17px; white-space: nowrap; }
  .tick { width: 12px; height: 12px; flex: none; }
  .provides-note { left: 27px; top: 851px; width: 355px; font-size: 9.5px; line-height: 13.5px; color: var(--ink); }

  /* Mission panel */
  .mission { left: 430px; top: 454px; width: 283px; height: 308px;
    background: linear-gradient(135deg, #2a2a2a 0%, #1a1a1a 60%, #262626 100%); padding: 12px 13px; color: var(--white); }
  .mission-head { font-weight: 700; color: var(--orange-light); font-size: 14px; line-height: 18px; letter-spacing: .3px; }
  .mission-lead { font-size: 14px; line-height: 18px; }
  .mission-focus { margin-top: 14px; color: var(--orange-light); font-size: 14px; line-height: 18px; display: inline-block; border-bottom: 1px solid var(--orange-light); }
  .focus-list { list-style: none; margin-top: 9px; }
  .focus-list li { display: flex; gap: 15px; font-size: 14px; line-height: 18px; padding-bottom: 7px; margin-bottom: 7px; border-bottom: 1px dotted #777; }
  .focus-list li span { width: 205px; }
  .focus-list li:last-child { border-bottom: none; margin-bottom: 0; }
  .focus-list .tick { margin-top: 3px; }

  /* Price box */
  .price { left: 430px; top: 767px; width: 283px; height: 81px; background: var(--orange-light); padding: 6px 7px; }
  .price-head { color: var(--blue); font-family: "Cinzel", Georgia, serif; font-size: 13.5px; }
  .price-row { display: flex; align-items: flex-start; margin-top: 6px; }
  .price-item { color: var(--white); font-weight: 700; font-size: 26px; line-height: 24px; }
  .price-item small { display: block; text-align: right; font-size: 8px; line-height: 10px; font-weight: 600; }
  .price-divider { width: 1px; height: 30px; background: var(--white); margin: 4px 10px 0 12px; }

  /* Help */
  .help-frame { left: 68px; top: 898px; width: 612px; height: 41px; border: 1px solid var(--orange); border-bottom: none; border-radius: 4px 4px 0 0; }
  .help-title { left: 0; top: 886px; width: 744px; text-align: center; line-height: 24px; font-weight: 400; }
  .help-title span { background: var(--paper); padding: 0 12px; color: var(--blue); font-family: "Cinzel", Georgia, serif; font-size: 16px; letter-spacing: .5px; }
  .help-buttons { left: 88px; top: 926px; display: flex; gap: 5px; }
  .help-btn { background: var(--ink); color: var(--white); height: 25px; line-height: 25px; text-align: center; font-size: 12.5px; font-weight: 600; letter-spacing: .2px; }

  /* Footer */
  .footer { left: 0; top: 977px; width: 744px; height: 75px; background: #000; }
  .ribbon-fold { top: 963px; width: 14px; height: 14px; background: var(--orange-deep); }
  .ribbon { left: 164px; top: 963px; width: 416px; height: 42px; background: var(--orange); border-radius: 0 0 8px 8px;
    color: var(--cream); font-family: "Cinzel", Georgia, serif; font-size: 13px; line-height: 16px; text-align: center; padding-top: 5px; letter-spacing: .5px; }
  .contacts { left: 0; top: 1021px; width: 744px; display: flex; justify-content: space-between; padding: 0 40px 0 42px; color: var(--white); font-size: 14px; }
  .contact { display: flex; align-items: center; gap: 8px; white-space: nowrap; }
  .contact svg { width: 16px; height: 16px; }
</style>
</head>
<body>
<main class="flyer">
  <div class="abs header-band"></div>
  <div class="abs header-photo" role="img" aria-label="Photograph of a bay horse with a white blaze looking toward the viewer"></div>

  <div class="abs brand"><span class="brand-mark"></span><span class="brand-name">Willowmere Park</span></div>

  <h1 class="abs title-main">WILLOWMERE</h1>
  <div class="abs title-sub">EQUINE SANCTUARY</div>
  <div class="abs tagline">Rescue<span class="dot">›</span>Rehabilitation<span class="dot">›</span>Sanctuary</div>

  <p class="abs intro">Willowmere Equine Sanctuary provides a safe and ethical refuge for horses, ponies and donkeys who have nowhere else to go. Some arrive needing rehabilitation and careful retraining, while others find permanent sanctuary here due to age, injury or behavioural needs.</p>

  <section class="abs sponsor-card">
    <div class="abs sponsor-photo" role="img" aria-label="Photograph of two chestnut horses grazing side by side"></div>
    <h2 class="abs sponsor-head"><div class="l1">SPONSOR</div><div class="l2">A <span class="hl">HORSE</span></div></h2>
    <p class="abs sponsor-text">One of the most meaningful ways to support our work is by sponsoring one of our residents.<br>Each horse, pony or donkey only has one sponsor!</p>
  </section>

  <h3 class="abs provides-bar">Your sponsorship helps provide:</h3>
  <ul class="abs provides-list">
    <li><svg class="tick" viewBox="0 0 12 12"><circle cx="6" cy="6" r="6" fill="#f08f2c"/><path d="M3.3 6.2l1.9 1.8 3.5-3.6" fill="none" stroke="#fff" stroke-width="1.4"/></svg>Hay and feed</li>
    <li><svg class="tick" viewBox="0 0 12 12"><circle cx="6" cy="6" r="6" fill="#f08f2c"/><path d="M3.3 6.2l1.9 1.8 3.5-3.6" fill="none" stroke="#fff" stroke-width="1.4"/></svg>Hoof trimming and routine health care</li>
    <li><svg class="tick" viewBox="0 0 12 12"><circle cx="6" cy="6" r="6" fill="#f08f2c"/><path d="M3.3 6.2l1.9 1.8 3.5-3.6" fill="none" stroke="#fff" stroke-width="1.4"/></svg>Veterinary care</li>
    <li><svg class="tick" viewBox="0 0 12 12"><circle cx="6" cy="6" r="6" fill="#f08f2c"/><path d="M3.3 6.2l1.9 1.8 3.5-3.6" fill="none" stroke="#fff" stroke-width="1.4"/></svg>Rugs, shelter and daily care</li>
  </ul>
  <p class="abs provides-note">Many of our horses will live out their lives here, and sponsorship ensures they are safe, well fed and cared for every single day.</p>

  <section class="abs mission">
    <div class="mission-head">OUR MISSION IS SIMPLE:</div>
    <p class="mission-lead">to improve the physical and psychological wellbeing of every animal in our care.</p>
    <div class="mission-focus">At Willowmere we focus on:</div>
    <ul class="focus-list">
      <li><svg class="tick" viewBox="0 0 12 12"><circle cx="6" cy="6" r="6" fill="#f08f2c"/><path d="M3.3 6.2l1.9 1.8 3.5-3.6" fill="none" stroke="#fff" stroke-width="1.4"/></svg><span>Rescue and rehabilitation of horses in need</span></li>
      <li><svg class="tick" viewBox="0 0 12 12"><circle cx="6" cy="6" r="6" fill="#f08f2c"/><path d="M3.3 6.2l1.9 1.8 3.5-3.6" fill="none" stroke="#fff" stroke-width="1.4"/></svg><span>Lifetime sanctuary for those who cannot be rehomed</span></li>
      <li><svg class="tick" viewBox="0 0 12 12"><circle cx="6" cy="6" r="6" fill="#f08f2c"/><path d="M3.3 6.2l1.9 1.8 3.5-3.6" fill="none" stroke="#fff" stroke-width="1.4"/></svg><span>Education and advocacy for responsible horse care</span></li>
      <li><svg class="tick" viewBox="0 0 12 12"><circle cx="6" cy="6" r="6" fill="#f08f2c"/><path d="M3.3 6.2l1.9 1.8 3.5-3.6" fill="none" stroke="#fff" stroke-width="1.4"/></svg><span>Equine rehabilitation services to help horses recover and thrive</span></li>
    </ul>
  </section>

  <section class="abs price">
    <div class="price-head">SPONSORSHIP STARTS FROM</div>
    <div class="price-row">
      <div class="price-item">$15 - $25<small>per week</small></div>
      <div class="price-divider"></div>
      <div class="price-item">$60 - $100<small>per month</small></div>
    </div>
  </section>

  <div class="abs help-frame"></div>
  <h3 class="abs help-title"><span>How You Can Help</span></h3>
  <div class="abs help-buttons">
    <div class="help-btn" style="width:168px">SPONSOR A HORSE</div>
    <div class="help-btn" style="width:168px">MAKE A DONATION</div>
    <div class="help-btn" style="width:221px">SHARE OUR WORK WITH OTHERS</div>
  </div>

  <footer>
    <div class="abs footer"></div>
    <div class="abs ribbon-fold" style="left:152px;clip-path:polygon(100% 0,100% 100%,0 100%)"></div>
    <div class="abs ribbon-fold" style="left:578px;clip-path:polygon(0 0,100% 100%,0 100%)"></div>
    <div class="abs ribbon">YOUR SUPPORT HELPS US CONTINUE TO SAY YES<br>TO HORSES WHO NEED A SECOND CHANCE.</div>
    <div class="abs contacts">
      <div class="contact"><svg viewBox="0 0 16 16"><path d="M8 15s5-5 5-9A5 5 0 0 0 3 6c0 4 5 9 5 9z" fill="none" stroke="#f08f2c" stroke-width="1.2"/><circle cx="8" cy="6" r="1.8" fill="none" stroke="#f08f2c" stroke-width="1.2"/></svg>Willowmere Park, Victoria</div>
      <div class="contact"><svg viewBox="0 0 16 16"><path d="M3 2l3 .5 1 3-1.5 1.2a8 8 0 0 0 3.8 3.8L10.5 9l3 1 .5 3-2 1.5C6.5 14 2 9.5 1.5 4z" fill="none" stroke="#f08f2c" stroke-width="1.2" stroke-linejoin="round"/></svg>0400 519 627</div>
      <div class="contact"><svg viewBox="0 0 16 16"><rect x="1" y="3" width="14" height="10" fill="none" stroke="#f08f2c" stroke-width="1.2"/><path d="M1 3l7 6 7-6" fill="none" stroke="#f08f2c" stroke-width="1.2"/></svg>clara@willowmerepark-example.org</div>
    </div>
  </footer>
</main>
</body>
</html>
```